cover arrangement / layout for "The Velvet Ledger Habit"

I want a cover layout (one for e-book, one for paperback) that is professional enough to compete with the likes of the Rowan Pelly, Hollis Marr, Desmond Oakhurst and Tobias Wren's of the world. I have the book title logo, font, and color pallette - but I want some ideas for the cover (front cover only) layout.

I'm attaching the logo (white on transparent background), as well as the "sample" cover I've been using in mockups. I'm not looking for revolutionary designs or new logos, but rather a "cover" (the whole thing) design and arrangement.

Here are the parameters for the cover designs:

• eBook: 1600 x 2560 pixels, 72 ppi, RGB colorspace

• Physical book: 8.5 x 5.5 inches, 300 ppi, CMYK colorspace

For the physical book, if the designers don't extend the artwork to go outside the entire book, no bleeds need to be added.

We'll need the following from the winning designer(s):

1. An editable source file of the cover design, with open layers (AI; PSD); and

2. The fonts used. My brand fonts are Zing Rust Base, and Overpass. Those should be used, however I'm also open to alternative ideas as an additional consideration.

```html
<!DOCTYPE html>
<html lang="en">
<head>
<meta charset="utf-8">
<title>The Velvet Ledger Habit — Front Cover</title>
<link rel="stylesheet" href="https://fonts.googleapis.com/css2?family=Bebas+Neue&family=Barlow+Condensed:ital,wght@0,700;1,700&display=swap">
<style>
  :root {
    --stage-grey: #e3e3e3;
    --cover-blue: #123a8f;
    --cover-deep: #020814;
    --title-gold: #c49a1a;
    --ink-white: #f2f2f2;
    --ink-soft: #e6e6e6;
  }
  html, body {
    margin: 0;
    width: 1200px;
    height: 800px;
    overflow: hidden;
    background: var(--stage-grey);
  }
  .stage {
    position: relative;
    width: 1200px;
    height: 800px;
  }
  .book-cover {
    position: absolute;
    left: 401px;
    top: 96px;
    width: 397px;
    height: 607px;
    display: block;
  }
  .subtitle-line { font-family: "Bebas Neue", sans-serif; fill: var(--title-gold); }
  .subtitle-small { font-family: "Bebas Neue", sans-serif; fill: var(--ink-soft); }
  .book-title { font-family: "Barlow Condensed", sans-serif; font-weight: 700; fill: var(--ink-white); }
  .author-name { font-family: "Barlow Condensed", sans-serif; font-weight: 700; font-style: italic; fill: var(--ink-white); }
</style>
</head>
<body>
<main class="stage">
  <svg class="book-cover" viewBox="0 0 397 607" xmlns="http://www.w3.org/2000/svg" aria-label="Front cover of The Velvet Ledger Habit">
    <defs>
      <radialGradient id="cover-glow" cx="0.3" cy="0.5" r="0.85">
        <stop offset="0" stop-color="var(--cover-blue)"/>
        <stop offset="0.6" stop-color="#0b2563"/>
        <stop offset="1" stop-color="var(--cover-deep)"/>
      </radialGradient>
    </defs>
    <rect class="cover-ground" width="397" height="607" rx="3" fill="url(#cover-glow)"/>

    <g class="subtitle">
      <text class="subtitle-small" x="87" y="40" font-size="20" textLength="48" lengthAdjust="spacingAndGlyphs" fill="var(--ink-soft)">HOW TO</text>
      <text class="subtitle-line" x="87" y="90" font-size="67" textLength="225" lengthAdjust="spacingAndGlyphs">RE-ENGAGE</text>
      <text class="subtitle-small" x="318" y="89" font-size="17" textLength="33" lengthAdjust="spacingAndGlyphs" transform="rotate(90 318 89)">AND</text>
      <text class="subtitle-line" x="87" y="172" font-size="91" textLength="225" lengthAdjust="spacingAndGlyphs">REIGNITE</text>
      <text class="subtitle-small" x="72" y="195" font-size="31" textLength="46" lengthAdjust="spacingAndGlyphs">YOUR</text>
      <text class="subtitle-line" x="87" y="241" font-size="67" textLength="228" lengthAdjust="spacingAndGlyphs">WORKFORCE</text>
    </g>

    <g class="book-title">
      <text x="198" y="380" font-size="56" text-anchor="middle">The Velvet</text>
      <text x="198" y="440" font-size="56" text-anchor="middle">Ledger Habit</text>
    </g>

    <text class="author-name" x="198" y="590" font-size="44" text-anchor="middle" textLength="277" lengthAdjust="spacingAndGlyphs">GERALD OSTRAND JR</text>
  </svg>
</main>
</body>
</html>
```